Electrician's Business needs web site for customers to get professional impression of business.

Have a logo, need a web page for customers to visit. Web page should make it easy for customers to approach /contact me, if possible a way for customers to leave their details so I can call them back.
A description/ list of services and advertise how my service is different and better than other electricians.
A gallery to upload photos to, to show completed works from past projects.
Updates

Target Market(s)

Domestic/residential home owner/renter/builder

Industry/Entity Type

Electrician

Coding

Coded - Design and coding required

Number of Pages Required

2 page

Font styles to use
Sans Serif

Colors
0255a3
ffffff

Requirements
Must have
• Appeal to home owner/renter, domestic market.
• Capture contact details of customer & advertise my contact details.
• List of services
Nice to have
• A photo gallery, so I can upload pictures of completed work.
Should not have
• Industrial/construction images.

```html
<!DOCTYPE html>
<html lang="en">
<head>
<meta charset="utf-8">
<title>Volt Mate | Electrical Services</title>
<link href="https://fonts.googleapis.com/css2?family=Montserrat:wght@400;500;600;700&display=swap" rel="stylesheet">
<style>
:root{
  --blue:#0255a3;
  --blue-deep:#0d4a94;
  --navy:#0a2f63;
  --orange:#f0821e;
  --white:#ffffff;
  --grey-head:#9a9a9a;
  --grey-text:#adadad;
  --grey-band:#e4e5e7;
  --line:#d9d9d9;
}
*{margin:0;padding:0;box-sizing:border-box}
html,body{width:1200px;height:2880px;overflow:hidden;background:var(--white)}
body{position:relative;font-family:"Montserrat",sans-serif;color:var(--grey-text)}
.abs{position:absolute}
.top-strip{left:0;top:0;width:1200px;height:12px;background:var(--blue)}
.brand{display:flex;align-items:center;gap:10px;color:var(--blue);font-weight:700;font-size:30px;letter-spacing:-.5px}
.brand .dot{width:14px;height:14px;border-radius:50%;background:var(--orange)}
.header-brand{left:130px;top:58px}
.phone-icon{left:764px;top:44px;width:28px;height:28px;border-radius:50%;background:var(--blue);display:flex;align-items:center;justify-content:center}
.phone-number{left:694px;top:80px;font-size:22px;font-weight:700;color:var(--blue)}
.btn{background:var(--orange);color:var(--white);font-size:13px;font-weight:500;display:flex;align-items:center;justify-content:center}
.quote-btn{left:927px;top:63px;width:140px;height:33px}
.nav-bar{left:0;top:117px;width:1200px;height:29px;background:var(--orange)}
.nav{left:405px;top:117px;height:29px;display:flex;font-size:12px;font-weight:600;color:var(--white)}
.nav a{display:flex;align-items:center;padding:0 14px;color:inherit;text-decoration:none}
.nav a.active{background:var(--blue-deep);padding:0 22px}
.hero{left:0;top:146px;width:1200px;height:440px;background:var(--blue-deep)}
.hero-photo{left:760px;top:146px;width:440px;height:440px;background:linear-gradient(90deg,var(--blue-deep) 0%,#3d6fae 30%,#6a8fc0 60%,#2c4f86 100%)}
.hero-welcome{left:134px;top:248px;font-size:35px;font-weight:500;color:var(--white)}
.hero-title{left:132px;top:287px;font-size:66px;font-weight:700;color:var(--white);letter-spacing:1px}
.hero-sub{left:134px;top:372px;width:420px;font-size:15px;font-weight:600;line-height:20px;color:var(--white)}
.hero-btn{top:436px;width:142px;height:34px;font-size:13px}
.dots{display:flex;gap:19px}
.dots span{width:14px;height:14px;border-radius:50%;background:var(--white)}
.hero-dots{left:561px;top:556px}
.social{left:1160px;top:234px;width:40px}
.social div{height:43px;display:flex;align-items:center;justify-content:center}
.section-title{left:0;width:1200px;text-align:center;font-size:37px;font-weight:700;color:var(--grey-head)}
.underline{left:515px;width:170px;height:3px;background:var(--orange)}
.para{left:134px;width:936px;text-align:center;font-size:14px;line-height:29px;color:var(--grey-text)}
.services-band{left:0;top:1117px;width:1200px;height:308px;background:var(--blue)}
.service-photo{top:1192px;height:167px}
.arrow{width:34px;height:31px;background:var(--navy);display:flex;align-items:center;justify-content:center}
.categories{left:361px;top:1671px;display:flex;gap:34px;font-size:14px;font-weight:700;color:var(--blue-deep);letter-spacing:.5px}
.categories span.active{border-bottom:2px solid var(--blue-deep);padding-bottom:2px}
.gallery-band{left:0;top:1716px;width:1200px;height:413px;background:var(--grey-band)}
.gallery{left:132px;top:1716px;width:936px;height:413px;display:grid;grid-template-columns:repeat(4,1fr);grid-template-rows:repeat(2,1fr)}
.gallery .tile{position:relative}
.tile-overlay{position:absolute;inset:8px;background:rgba(2,85,163,.85);display:flex;flex-direction:column;justify-content:center;padding:0 20px;color:var(--white);text-align:center}
.tile-overlay p{font-size:11px;line-height:15px}
.tile-overlay h4{font-size:20px;font-weight:700;margin-top:6px}
.testimonial{left:132px;top:2339px;width:936px;height:105px;background:var(--blue);color:var(--white);text-align:center;display:flex;flex-direction:column;justify-content:center;align-items:center}
.testimonial p{width:760px;font-size:13.5px;line-height:20px;letter-spacing:-.2px}
.testimonial .name{margin-top:6px;font-size:14px;font-weight:700;line-height:18px}
.quote-mark{top:34px;font-size:56px;font-weight:700;line-height:40px;font-family:Georgia,serif}
.grey-dots span{background:#bdbdbd}
.foot-head{top:2528px;font-size:13px;font-weight:700;color:var(--grey-head);letter-spacing:.5px}
.foot-text{font-size:13px;line-height:20px;color:var(--grey-head)}
.service-list{left:365px;top:2557px;width:196px;font-size:13px;color:var(--grey-head)}
.service-list li{list-style:none;height:31px;line-height:31px;border-bottom:1px solid var(--line)}
.contact{left:599px;top:2565px;font-size:13px;line-height:23px;color:var(--grey-head)}
.contact .link{color:var(--blue);font-weight:500}
.field{left:833px;width:235px;border:1px solid #d6d6d6;font-size:12px;color:var(--grey-head);padding:5px 8px}
.field.focus{border-color:var(--blue)}
.bottom-bar{left:0;top:2836px;width:1200px;height:44px;background:var(--blue);color:var(--white);font-size:14px;display:flex;align-items:center;justify-content:center}
</style>
</head>
<body>
<div class="abs top-strip"></div>

<header>
  <div class="abs brand header-brand"><span class="dot"></span>Volt Mate</div>
  <div class="abs phone-icon">
    <svg width="14" height="14" viewBox="0 0 24 24"><path fill="#f0821e" d="M6.6 10.8a15.1 15.1 0 0 0 6.6 6.6l2.2-2.2c.3-.3.7-.4 1-.2 1.1.4 2.3.6 3.6.6.6 0 1 .4 1 1V20c0 .6-.4 1-1 1A17 17 0 0 1 3 4c0-.6.4-1 1-1h3.5c.6 0 1 .4 1 1 0 1.3.2 2.5.6 3.6.1.3 0 .7-.2 1z"/></svg>
  </div>
  <div class="abs phone-number">1-800-555-0188</div>
  <div class="abs btn quote-btn">Get a Quote</div>
  <div class="abs nav-bar"></div>
  <nav class="abs nav">
    <a class="active">HOME</a><a>ABOUT US</a><a>OUR SERVICES</a><a>CONTACT US</a>
  </nav>
</header>

<section>
  <div class="abs hero"></div>
  <div class="abs hero-photo" role="img" aria-label="Electrician in blue overalls testing wiring with a multimeter"></div>
  <div class="abs hero-welcome">Welcome to</div>
  <div class="abs hero-title">VOLT MATE</div>
  <div class="abs hero-sub">Electrical Services for the industrial, commercial and domestic sectors.</div>
  <div class="abs btn hero-btn" style="left:131px">Read More</div>
  <div class="abs btn hero-btn" style="left:294px">Our Services</div>
  <div class="abs dots hero-dots"><span></span><span></span><span></span></div>
  <div class="abs social">
    <div style="background:#2c4f8f"></div>
    <div style="background:#2aa3df"></div>
    <div style="background:#1fb79a"><svg width="18" height="13" viewBox="0 0 18 13"><rect x="1" y="1" width="16" height="11" fill="none" stroke="#fff" stroke-width="1.6"/><path d="M1 1l8 6 8-6" fill="none" stroke="#fff" stroke-width="1.6"/></svg></div>
    <div style="background:#e8513d"><svg width="12" height="17" viewBox="0 0 12 17"><path d="M6 0a6 6 0 0 1 6 6c0 4.5-6 11-6 11S0 10.5 0 6a6 6 0 0 1 6-6z" fill="#fff"/><circle cx="6" cy="6" r="2.2" fill="#e8513d"/></svg></div>
    <div style="background:#8a6a4e"></div>
  </div>
</section>

<section>
  <h2 class="abs section-title" style="top:613px">About Us</h2>
  <div class="abs underline" style="top:662px"></div>
  <p class="abs para" style="top:696px">It is a long established fact that a reader will be distracted by the readable content of a page when looking at its layout. The point of using Lorem Ipsum is that it has a more-or-less normal distribution of letters, as opposed to using 'Content here, content here', making it look like readable English. Many desktop publishing packages and web page editors now use Lorem Ipsum as their default model text, and a search for 'lorem ipsum' will uncover many web sites still in their infancy. Various versions have evolved over the years, sometimes by accident, sometimes on purpose (injected humour and the like).</p>
  <div class="abs btn" style="left:532px;top:862px;width:140px;height:35px">Read More</div>
</section>

<section>
  <h2 class="abs section-title" style="top:928px">Our Services</h2>
  <div class="abs underline" style="top:975px"></div>
  <p class="abs para" style="top:1017px">It is a long established fact that a reader will be distracted by the readable content of a page when looking at its layout. The point of using Lorem Ipsum is that it has a more-or-less normal distribution of letters, as opposed to using 'Content here, content here', making it look like readable English.</p>
  <div class="abs services-band"></div>
  <div class="abs arrow" style="left:98px;top:1256px"><svg width="12" height="10" viewBox="0 0 12 10"><path d="M11 5H2M5 1L1 5l4 4" fill="none" stroke="#fff" stroke-width="2"/></svg></div>
  <div class="abs service-photo" style="left:167px;width:253px;background:linear-gradient(135deg,#c8a15a,#7d6a4d 60%,#4a5a7a)" role="img" aria-label="Electrician explaining a fuse board to a homeowner"></div>
  <div class="abs service-photo" style="left:490px;width:217px;background:linear-gradient(135deg,#8b8f8c,#b7b3a6 50%,#5c6b6e)" role="img" aria-label="Hands wiring an open distribution panel"></div>
  <div class="abs service-photo" style="left:801px;width:217px;background:linear-gradient(135deg,#e8e4de,#c9b8a3 50%,#7f6a5a)" role="img" aria-label="Electrician connecting coloured cables in a ceiling"></div>
  <div class="abs arrow" style="left:1068px;top:1256px"><svg width="12" height="10" viewBox="0 0 12 10"><path d="M1 5h9M7 1l4 4-4 4" fill="none" stroke="#fff" stroke-width="2"/></svg></div>
</section>

<section>
  <h2 class="abs section-title" style="top:1470px">Recent Projects</h2>
  <div class="abs underline" style="top:1519px"></div>
  <p class="abs para" style="top:1553px">It is a long established fact that a reader will be distracted by the readable content of a page when looking at its layout. The point of using Lorem Ipsum is that it has a more-or-less normal distribution of letters, as opposed to using 'Content here, content here', making it look like readable English.</p>
  <div class="abs categories"><span class="active">CATEGORY 1</span><span>CATEGORY 2</span><span>CATEGORY 3</span><span>CATEGORY 4</span></div>
  <div class="abs gallery-band"></div>
  <div class="abs gallery">
    <div class="tile" style="background:linear-gradient(135deg,#3b6fae,#7b9cc4)" role="img" aria-label="Completed switchboard installation">
      <div class="tile-overlay"><p>Rewiring and new consumer unit fitted for a family home in two days.</p><h4>Project Name</h4></div>
    </div>
    <div class="tile" style="background:linear-gradient(135deg,#9a9a9a,#d9b64a 50%,#555)" role="img" aria-label="Gloved hands fitting circuit breakers"></div>
    <div class="tile" style="background:linear-gradient(135deg,#b04a3a,#d9c24a 50%,#3a4a5a)" role="img" aria-label="Multimeter testing a breaker panel"></div>
    <div class="tile" style="background:linear-gradient(135deg,#6a7f8a,#c9a98a 50%,#333)" role="img" aria-label="Hands holding a digital multimeter"></div>
    <div class="tile" style="background:linear-gradient(135deg,#d9c14a,#4a5a6a 50%,#b0b5b8)" role="img" aria-label="Testing wiring with a yellow multimeter"></div>
    <div class="tile" style="background:linear-gradient(135deg,#e6c02a,#7a5a48 50%,#3a3a3a)" role="img" aria-label="Electrician in hard hat working on a panel"></div>
    <div class="tile" style="background:linear-gradient(135deg,#2a3f6a,#8a7a6a 50%,#b9b3a6)" role="img" aria-label="Electrician inspecting a wall fuse box"></div>
    <div class="tile" style="background:linear-gradient(135deg,#d8d8d8,#c9a58a 50%,#6a6a6a)" role="img" aria-label="Voltage tester used on wall wiring"></div>
  </div>
</section>

<section>
  <h2 class="abs section-title" style="top:2155px">Testimonials</h2>
  <div class="abs underline" style="top:2202px"></div>
  <p class="abs para" style="top:2236px">It is a long established fact that a reader will be distracted by the readable content of a page when looking at its layout. The point of using Lorem Ipsum is that it has a more-or-less normal distribution of letters, as opposed to using 'Content here, content here', making it look like readable English.</p>
  <div class="abs testimonial">
    <span class="abs quote-mark" style="left:44px">&ldquo;</span>
    <p>It is a long established fact that a reader will be distracted by the readable content of a page when looking at its layout. The point of using Lorem Ipsum is that it has a more-or-less normal distribution.</p>
    <div class="name">Mr. Aldren</div>
    <span class="abs quote-mark" style="left:860px">&rdquo;</span>
  </div>
  <div class="abs dots grey-dots" style="left:561px;top:2466px"><span></span><span></span><span></span></div>
</section>

<footer>
  <div class="abs foot-head" style="left:132px">ABOUT COMPANY</div>
  <div class="abs brand" style="left:132px;top:2570px;font-size:26px"><span class="dot"></span>Volt Mate</div>
  <p class="abs foot-text" style="left:132px;top:2638px;width:210px">Lorem ipsum dolor sit amet, con adipiscing elit. Aenean ac libor eu lobortis risus. Nunc bibendum eros iac dui dig eget accumsan magna tristique.</p>

  <div class="abs foot-head" style="left:365px">SERVICES</div>
  <ul class="abs service-list">
    <li>Industrial &amp; Building</li>
    <li>Electrification.</li>
    <li>Planning &amp; Installation.</li>
    <li>Installation of H.T. Panel.</li>
    <li>Installation of L.T. Panel</li>
    <li style="border-bottom:none">Installation of Light Fixtures.</li>
  </ul>

  <div class="abs foot-head" style="left:599px">CONTACT US</div>
  <div class="abs contact">
    Bristol, UK<br>41, Elm Row, Ashford Vale<br><br>Tel: (888) 555-0142<br>Mobile: (012) 555-0177<br><br>E-mail: hello@voltmate.example<br><span class="link">Get directions on the map</span>
  </div>

  <div class="abs foot-head" style="left:833px">GET FREE QUOTE</div>
  <div class="abs field focus" style="top:2559px;height:27px">Name</div>
  <div class="abs field" style="top:2594px;height:27px">Email</div>
  <div class="abs field" style="top:2632px;height:27px;display:flex;justify-content:space-between">Service<svg width="10" height="8" viewBox="0 0 10 8" style="margin-top:4px"><path d="M0 0h10L5 7z" fill="#9a9a9a"/></svg></div>
  <div class="abs field" style="top:2671px;height:79px">Message</div>
  <div class="abs btn" style="left:833px;top:2772px;width:140px;height:33px;font-size:14px">Send</div>

  <div class="abs bottom-bar">&copy; 2016 Volt Mate | Electrical Services !</div>
</footer>
</body>
</html>
```